Plumbing Service Flyer Needed For Swapnook

Plumbing ad needs to be effective (600 by 450 pixels)
Ad must include company name Kestrel Drainworks and phone number 404-555-0183
No URLs, links, or web addresses in your text or image please.

(about us we offer a wide range of plumbing services from emergency plumbing to commercial plumbing services, our master plumbers are ready to handle all jobs, large or small, at anytime during the day or night. Pickup the phone and call us today).

Target Market(s)

DC Metro Area

Industry/Entity Type

Plumbing

Font styles to use
Other font styles liked:
• No preference. Let the designer choose

Colors

Designer to choose colors to be used in the design.

Requirements
Must have
• 1. A bold headline: headline should communicate what my business is all about.
• 2. Great photography
• 3. Discounts or specials
• 4. Call to action
• 5. Key facts: Let consumers know about the product or service (see attached ad)
• 6. Good graphics
Should not have
• No URLs, links, or web addresses in your text or image please.

```html
<!DOCTYPE html>
<html lang="en">
<head>
<meta charset="utf-8">
<title>Kestrel Drainworks – Plumbing Flyer Options</title>
<link href="https://fonts.googleapis.com/css2?family=Bebas+Neue&family=Lato:ital,wght@0,400;0,700;1,400;1,700&family=Oswald:wght@600&display=swap" rel="stylesheet">
<style>
:root{
  --board:#2a2a2a;
  --navy:#1d2a5c;
  --royal:#1f4f9e;
  --teal:#0e5878;
  --yellow:#fcd116;
  --red:#d8232f;
  --orange:#f05a28;
  --ink:#1b1b1b;
  --white:#ffffff;
  --photo-a:#3b4a7a;
  --photo-b:#28345e;
}
*{box-sizing:border-box;margin:0;padding:0}
html,body{width:775px;height:1200px;overflow:hidden;background:var(--board)}
body{position:relative;font-family:'Lato',sans-serif}
.option-number{position:absolute;font-family:'Bebas Neue',sans-serif;color:var(--white);font-size:118px;line-height:1}
.flyer{position:absolute;width:490px;height:367px;overflow:hidden}
.flyer > *{position:absolute}
.flyer svg.shapes{left:0;top:0;width:490px;height:367px}
.display{font-family:'Bebas Neue',sans-serif;line-height:1;white-space:nowrap}
.subhead{font-family:'Oswald',sans-serif;font-weight:600;line-height:1;white-space:nowrap;text-transform:uppercase}
.photo{border-radius:4px;background:linear-gradient(180deg,var(--photo-a),var(--photo-b))}
.about-title{font-family:'Bebas Neue',sans-serif;font-size:11px;line-height:1;margin-bottom:3px}
.about-text{font-size:7.6px;line-height:1.3;text-align:justify}
.services-title{font-family:'Bebas Neue',sans-serif;font-size:10.5px;line-height:1}
.service-columns{display:grid;margin-top:6px}
.service-list{list-style:none;font-size:7px;font-style:italic;line-height:11.6px}
.service-list li{position:relative;padding-left:12px}
.service-list li::before{content:"";position:absolute;left:0;top:3px;width:6px;height:6px;border-radius:50%;background:var(--dot)}
.service-list .more{font-size:6.5px}
.service-list .more::before{display:none}
.phone-row{display:flex;align-items:center;gap:6px}

/* Flyer 1 */
.flyer-yellow{left:22px;top:27px;background:var(--navy)}
.flyer-yellow .topbar{left:0;top:0;width:490px;height:56px;background:var(--yellow)}
.flyer-yellow .headline{left:22px;top:12px;font-size:45px;color:var(--ink)}
.flyer-yellow .headline span{color:var(--white);margin-left:9px}
.flyer-yellow .about{left:188px;top:70px;width:264px;color:var(--white)}
.flyer-yellow .about-title,.flyer-yellow .services-title,.flyer-yellow .more{color:var(--yellow)}
.flyer-yellow .services{left:236px;top:116px;color:var(--white);--dot:var(--yellow)}
.flyer-yellow .service-columns{grid-template-columns:115px auto}
.flyer-yellow .company{left:17px;top:233px;font-size:29px;color:var(--navy)}
.flyer-yellow .bonded{left:17px;top:262px;font-size:8px;color:var(--white);font-weight:700}
.flyer-yellow .cta{left:17px;top:277px;font-size:17px;color:var(--navy)}
.flyer-yellow .phone{left:17px;top:296px;font-size:44px;color:var(--ink)}

/* Flyer 2 */
.flyer-blue{left:217px;top:421px;background:linear-gradient(160deg,#2a63b8,var(--royal) 55%,#173f86)}
.flyer-blue .headline{left:182px;top:14px;font-size:62px;color:var(--white)}
.flyer-blue .subhead{left:179px;top:68px;font-size:34px;color:var(--red);-webkit-text-stroke:0.8px var(--white)}
.flyer-blue .about{left:208px;top:107px;width:267px;color:var(--white)}
.flyer-blue .about-text{font-size:8px}
.flyer-blue .services{left:234px;top:163px;color:var(--white);--dot:var(--red)}
.flyer-blue .service-columns{grid-template-columns:123px auto}
.flyer-blue .more{color:var(--red)}
.flyer-blue .cta{left:353px;top:264px;font-size:17px;color:var(--white)}
.flyer-blue .cta span{font-size:25px}
.flyer-blue .phone{left:211px;top:298px;font-size:44px;color:var(--white)}

/* Flyer 3 */
.flyer-teal{left:22px;top:807px;background:var(--teal)}
.flyer-teal .headline{left:20px;top:17px;font-size:62px;color:var(--white)}
.flyer-teal .subhead{left:20px;top:70px;font-size:34px;color:var(--orange)}
.flyer-teal .about{left:20px;top:117px;width:258px;color:var(--white)}
.flyer-teal .about-text{font-size:8px}
.flyer-teal .about-title,.flyer-teal .services-title{color:var(--orange)}
.flyer-teal .services{left:20px;top:165px;color:var(--white);--dot:var(--orange)}
.flyer-teal .service-columns{grid-template-columns:120px auto}
.flyer-teal .more{color:var(--orange)}
.flyer-teal .footer-left{left:0;top:303px;width:242px;height:47px;background:var(--white)}
.flyer-teal .footer-right{left:242px;top:303px;width:248px;height:47px;background:#2a2a2a}
.flyer-teal .footer-strip{left:0;top:350px;width:490px;height:17px;background:linear-gradient(90deg,#e8501f,var(--orange) 50%,#c9401a)}
.flyer-teal .cta{left:17px;top:317px;font-size:19px;color:var(--ink)}
.flyer-teal .phone{left:253px;top:309px;font-size:37px;color:var(--white)}
</style>
</head>
<body>

<div class="option-number" style="left:530px;top:50px">1</div>
<div class="option-number" style="left:132px;top:459px">2</div>
<div class="option-number" style="left:552px;top:833px">3</div>

<!-- Option 1 -->
<section class="flyer flyer-yellow">
  <div class="topbar"></div>
  <div class="photo" role="img" aria-label="Photo of a plumber in a yellow hard hat and navy overalls holding a red pipe wrench" style="left:45px;top:56px;width:150px;height:160px"></div>
  <svg class="shapes" viewBox="0 0 490 367" aria-hidden="true">
    <path d="M0 232 C95 208 195 210 272 252 C325 282 400 314 490 318 L490 346 L0 346 Z" fill="var(--yellow)"/>
    <path d="M0 224 C95 200 198 202 278 245" fill="none" stroke="#111" stroke-width="8"/>
    <path d="M0 217 C97 192 202 194 284 238" fill="none" stroke="#fff" stroke-width="5"/>
    <path d="M30 210 C140 185 230 195 300 245 L310 238 C235 185 140 174 30 200 Z" fill="#1f5fb5"/>
    <rect x="0" y="346" width="490" height="21" fill="#1f5fb5"/>
    <path d="M266 214 L345 204 L424 214 L420 300 C404 320 372 332 345 341 C318 332 286 320 270 300 Z" fill="#1f5fb5"/>
    <path d="M273 219 L345 210 L417 219 L413 297 C398 315 370 326 345 334 C320 326 292 315 277 297 Z" fill="#e9ecef" stroke="#fff" stroke-width="2"/>
    <text x="345" y="242" text-anchor="middle" font-family="Bebas Neue, sans-serif" font-size="23" fill="var(--red)">Special Offer</text>
    <text x="334" y="283" text-anchor="middle" font-family="Bebas Neue, sans-serif" font-size="46" fill="var(--ink)">$25</text>
    <text x="377" y="268" text-anchor="middle" font-family="Bebas Neue, sans-serif" font-size="16" fill="var(--ink)" transform="rotate(90 377 268)">OFF</text>
    <text x="345" y="299" text-anchor="middle" font-family="Bebas Neue, sans-serif" font-size="15" fill="var(--red)">Any Plumbing Service</text>
    <text x="345" y="309" text-anchor="middle" font-family="Lato, sans-serif" font-style="italic" font-size="6" fill="var(--ink)">*Offer Applies to projects</text>
    <text x="345" y="317" text-anchor="middle" font-family="Lato, sans-serif" font-style="italic" font-size="6" fill="var(--ink)">$250 or more</text>
  </svg>
  <div class="display headline">24/7 Plumber<span>At Your Service!</span></div>
  <div class="about">
    <div class="about-title">About Us</div>
    <p class="about-text">we offer a wide range of plumbing services from emergency plumbing to commercial plumbing services, our master plumbers are ready to handle all jobs, large or small, at anytime during the day or night.</p>
  </div>
  <div class="services">
    <div class="services-title">Here are a few of my plumbing services:</div>
    <div class="service-columns">
      <ul class="service-list"><li>Plumbing clogs</li><li>Water heater replacement</li><li>Repair and install gas lines</li><li>Remodel your plumbing</li><li>Flood repair</li></ul>
      <ul class="service-list"><li>Disposals repair and install</li><li>Toilets install or replace</li><li>New piping and repairs</li><li>New homes, old homes,<br>commercial plumbing</li><li class="more">and a ton more</li></ul>
    </div>
  </div>
  <div class="display company">Kestrel Drainworks</div>
  <div class="bonded">BONDED, LICENSED AND INSURED</div>
  <div class="display cta">Pickup the phone and call us today</div>
  <div class="display phone phone-row">
    <svg width="30" height="30" viewBox="0 0 30 30" aria-hidden="true"><circle cx="15" cy="15" r="12" fill="none" stroke="#fff" stroke-width="2.5"/><path d="M6 7 L10 5 L12 10 L9.5 12 C10.5 15 13 17.5 16 19 L18 16.5 L23 19 L21 23 C13 23 6 16 6 7Z" fill="#fff"/></svg>
    <span>404-555-0183</span>
  </div>
</section>

<!-- Option 2 -->
<section class="flyer flyer-blue">
  <div class="photo" role="img" aria-label="Photo of a plumber in a yellow hard hat and navy overalls holding a red pipe wrench" style="left:17px;top:17px;width:180px;height:258px"></div>
  <svg class="shapes" viewBox="0 0 490 367" aria-hidden="true">
    <path d="M0 302 C120 322 210 292 280 272 C360 252 430 248 490 246 L490 258 C430 260 360 266 280 286 C210 306 120 338 0 318Z" fill="#fff"/>
    <path d="M0 318 C120 338 210 306 280 286 C360 266 430 260 490 258 L490 367 L0 367Z" fill="var(--red)"/>
    <path d="M0 330 C80 352 160 340 230 310 C170 350 110 367 70 367 L0 367Z" fill="#fff"/>
    <path d="M0 348 C60 362 120 358 180 340 C140 362 115 367 100 367 L0 367Z" fill="#1a3f86"/>
    <circle cx="94" cy="296" r="55" fill="#2b2b2b"/>
    <circle cx="94" cy="296" r="51" fill="#fff"/>
    <circle cx="94" cy="296" r="47" fill="var(--yellow)"/>
    <text x="94" y="272" text-anchor="middle" font-family="Bebas Neue, sans-serif" font-size="15" fill="var(--red)">Special Offer</text>
    <text x="87" y="306" text-anchor="middle" font-family="Bebas Neue, sans-serif" font-size="37" fill="var(--ink)">$25</text>
    <text x="121" y="293" text-anchor="middle" font-family="Bebas Neue, sans-serif" font-size="13" fill="var(--ink)" transform="rotate(90 121 293)">OFF</text>
    <text x="94" y="318" text-anchor="middle" font-family="Bebas Neue, sans-serif" font-size="10" fill="var(--red)">Any Plumbing Service</text>
    <text x="94" y="327" text-anchor="middle" font-family="Lato, sans-serif" font-style="italic" font-size="5.5" fill="var(--ink)">*Offer Applies to projects</text>
    <text x="94" y="334" text-anchor="middle" font-family="Lato, sans-serif" font-style="italic" font-size="5.5" fill="var(--ink)">$250 or more</text>
  </svg>
  <div class="display headline">24/7 Plumber</div>
  <div class="subhead">At Your Service!</div>
  <div class="about">
    <div class="about-title">About Us</div>
    <p class="about-text">We offer a wide range of plumbing services from emergency plumbing to commercial plumbing services, our master plumbers are ready to handle all jobs, large or small, at anytime during the day or night.</p>
  </div>
  <div class="services">
    <div class="services-title">Here are a few of my plumbing services:</div>
    <div class="service-columns">
      <ul class="service-list"><li>Plumbing clogs</li><li>Water heater replacement</li><li>Repair and install gas lines</li><li>Remodel your plumbing</li><li>Flood repair</li></ul>
      <ul class="service-list"><li>Disposals repair and install</li><li>Toilets install or replace</li><li>New piping and repairs</li><li>New homes, old homes,<br>commercial plumbing</li><li class="more">and a ton more</li></ul>
    </div>
  </div>
  <div class="display cta">Pickup the phone and<br><span>call us today</span></div>
  <div class="display phone phone-row">
    <svg width="30" height="30" viewBox="0 0 30 30" aria-hidden="true"><circle cx="15" cy="15" r="12" fill="none" stroke="#fff" stroke-width="2.5"/><path d="M6 7 L10 5 L12 10 L9.5 12 C10.5 15 13 17.5 16 19 L18 16.5 L23 19 L21 23 C13 23 6 16 6 7Z" fill="#fff"/></svg>
    <span>(202) 555-0147</span>
  </div>
</section>

<!-- Option 3 -->
<section class="flyer flyer-teal">
  <div class="photo" role="img" aria-label="Photo of a plumber in a yellow hard hat and navy overalls holding a red pipe wrench" style="left:312px;top:18px;width:176px;height:262px"></div>
  <svg class="shapes" viewBox="0 0 490 367" aria-hidden="true">
    <path d="M0 244 C110 292 330 296 490 226 L490 236 C330 302 110 300 0 255Z" fill="#fff"/>
    <path d="M0 255 C110 300 330 302 490 236 L490 244 C330 308 110 306 0 264Z" fill="#1b1b1b"/>
    <path d="M0 264 C110 306 330 308 490 244 L490 303 L0 303Z" fill="var(--orange)"/>
    <path d="M145 298 C148 270 175 253 205 252 L290 252 C315 253 330 270 330 298Z" fill="var(--yellow)"/>
    <text x="200" y="284" text-anchor="middle" font-family="Bebas Neue, sans-serif" font-size="36" fill="var(--red)">$25</text>
    <text x="230" y="274" text-anchor="middle" font-family="Bebas Neue, sans-serif" font-size="11" fill="var(--ink)" transform="rotate(90 230 274)">OFF</text>
    <text x="239" y="270" font-family="Bebas Neue, sans-serif" font-size="13" fill="var(--ink)">Any Plumbing</text>
    <text x="239" y="285" font-family="Bebas Neue, sans-serif" font-size="17" fill="var(--ink)">Service</text>
    <text x="238" y="295" text-anchor="middle" font-family="Lato, sans-serif" font-style="italic" font-size="5.5" fill="var(--ink)">*Offer Applies to projects $250 or more</text>
  </svg>
  <div class="display headline">24/7 Plumber</div>
  <div class="subhead">At Your Service!</div>
  <div class="about">
    <div class="about-title">About Us</div>
    <p class="about-text">We offer a wide range of plumbing services from emergency plumbing to commercial plumbing services, our master plumbers are ready to handle all jobs, large or small, at anytime during the day or night.</p>
  </div>
  <div class="services">
    <div class="services-title">Here are a few of my plumbing services:</div>
    <div class="service-columns">
      <ul class="service-list"><li>Plumbing clogs</li><li>Water heater replacement</li><li>Repair and install gas lines</li><li>Remodel your plumbing</li><li>Flood repair</li></ul>
      <ul class="service-list"><li>Disposals repair and install</li><li>Toilets install or replace</li><li>New piping and repairs</li><li>New homes, old homes,<br>commercial plumbing</li><li class="more">and a ton more</li></ul>
    </div>
  </div>
  <div class="footer-left"></div>
  <div class="footer-right"></div>
  <div class="footer-strip"></div>
  <div class="display cta">Pickup the phone and call us today</div>
  <div class="display phone phone-row">
    <svg width="26" height="26" viewBox="0 0 30 30" aria-hidden="true"><circle cx="15" cy="15" r="12" fill="none" stroke="#fff" stroke-width="2.5"/><path d="M6 7 L10 5 L12 10 L9.5 12 C10.5 15 13 17.5 16 19 L18 16.5 L23 19 L21 23 C13 23 6 16 6 7Z" fill="#fff"/></svg>
    <span>(571) 555-0129</span>
  </div>
</section>

</body>
</html>
```